New modern business card design

To design a brand new business card that's clean & modern in terms of layout.
I have attached our company logo and also basic information regarding what is needed on the card that also needs to be editable.

Target Market(s)

motor trade

Contact Information for Business Card

logo, name, title, tel, mob, email, address, www, all information is in the word.doc file

Requirements
Must have
• white background
Nice to have
• Nice clean font

```html
<!DOCTYPE html>
<html lang="en">
<head>
<meta charset="utf-8">
<title>Torque Works Ltd – Business Card</title>
<link rel="stylesheet" href="https://fonts.googleapis.com/css2?family=Archivo:wght@400;500;800&display=swap">
<style>
  :root {
    --page-bg: #dcdad6;
    --card-bg: #ffffff;
    --brand-blue: #1b7fc0;
    --charcoal: #3a3c40;
    --icon-grey: #6e7074;
  }
  * { box-sizing: border-box; margin: 0; padding: 0; }
  html, body { width: 1200px; height: 798px; overflow: hidden; }
  body {
    background: var(--page-bg);
    font-family: "Archivo", Arial, sans-serif;
    display: flex;
    align-items: center;
    justify-content: center;
  }
  .business-card {
    position: relative;
    width: 1000px;
    height: 647px;
    background: var(--card-bg);
    border-radius: 6px;
    box-shadow: 0 10px 28px rgba(0,0,0,.18);
  }
  .brand {
    position: absolute;
    top: 110px;
    left: 0;
    right: 0;
    display: flex;
    justify-content: center;
    align-items: center;
    gap: 14px;
    padding-left: 150px;
  }
  .brand-mark {
    width: 34px;
    height: 34px;
    background: var(--brand-blue);
  }
  .brand-name {
    color: var(--brand-blue);
    font-weight: 500;
    font-size: 36px;
    letter-spacing: 2px;
  }
  .person-name {
    position: absolute;
    top: 210px;
    left: 130px;
    font-weight: 800;
    font-size: 96px;
    letter-spacing: -1px;
    line-height: 1;
  }
  .first-name { color: var(--brand-blue); }
  .last-name { color: var(--charcoal); }
  .job-title {
    position: absolute;
    top: 312px;
    left: 330px;
    color: var(--brand-blue);
    font-weight: 500;
    font-size: 36px;
  }
  .contact-list {
    position: absolute;
    top: 380px;
    left: 90px;
    list-style: none;
  }
  .contact-item {
    display: flex;
    align-items: center;
    gap: 22px;
    height: 44px;
    color: var(--brand-blue);
    font-size: 30px;
  }
  .contact-icon {
    width: 28px;
    height: 28px;
    flex: none;
    fill: none;
    stroke: var(--icon-grey);
    stroke-width: 2;
  }
  .contact-icon .solid { fill: var(--icon-grey); stroke: none; }
</style>
</head>
<body>
  <article class="business-card">
    <header class="brand">
      <span class="brand-mark"></span>
      <span class="brand-name">TORQUE WORKS LTD</span>
    </header>

    <h1 class="person-name"><span class="first-name">Daniel</span> <span class="last-name">Harper</span></h1>
    <p class="job-title">General Manager</p>

    <ul class="contact-list">
      <li class="contact-item">
        <svg class="contact-icon" viewBox="0 0 24 24"><path class="solid" d="M6.6 3.5l2.6 3.8-1.8 2.1c1.1 2.5 3.1 4.5 5.6 5.6l2.1-1.8 3.8 2.6-1.6 3.2C10.5 19 5 13.5 3.4 6.7z"/></svg>
        <span>0161 555 0192</span>
      </li>
      <li class="contact-item">
        <svg class="contact-icon" viewBox="0 0 24 24"><rect x="7" y="3" width="10" height="18" rx="2"/><line x1="11" y1="18" x2="13" y2="18"/></svg>
        <span>07700 900 418</span>
      </li>
      <li class="contact-item">
        <svg class="contact-icon" viewBox="0 0 24 24"><circle cx="12" cy="12" r="4"/><path d="M16 8v5.5a2.5 2.5 0 0 0 5 0V12a9 9 0 1 0-3.5 7.1"/></svg>
        <span>dharper@torque-works.co.uk</span>
      </li>
      <li class="contact-item">
        <svg class="contact-icon" viewBox="0 0 24 24"><path class="solid" d="M12 3l10 9h-3v9h-5v-6h-4v6H5v-9H2z"/></svg>
        <span>Mill Lane, Failsworth, Manchester, M35 0QX</span>
      </li>
      <li class="contact-item">
        <svg class="contact-icon" viewBox="0 0 24 24"><circle cx="12" cy="12" r="9"/><ellipse cx="12" cy="12" rx="4" ry="9"/><line x1="3" y1="12" x2="21" y2="12"/><path d="M5 7h14M5 17h14"/></svg>
        <span>www.torque-works.co.uk</span>
      </li>
    </ul>
  </article>
</body>
</html>
```